KORVANE THERAPEUTICS

physical therapy company. need a flashy image and named logo, website link, that I can also use on Letterhead and business cards. Clean, sharp, modern, eye catching. 3 colors? Some shine. Needs to stand out and not be trendy or too much cursive . Androgynous image of a human body is ok. A spine included is ok. Prefer lines to curves for font types. Warm colors but strong impact. Will need to have some contact info and border mission statement on it.

Target Market(s)

Target market is large corporations, wealthy individuals, medical doctors

Industry/Entity Type

Medical, physical therapy

Contact Information for Business Card

Name, Owner, phone, email, and website

Colors
0054AA
0677BA
7BADD7
CADEEF
E8F1F8

Requirements
Must have
• See above- something about BALANCE, wellness, strength etc
Nice to have
• Contrast, depth
Should not have
• No cursive

```html
<!DOCTYPE html>
<html lang="en">
<head>
<meta charset="utf-8">
<title>Korvane Therapeutics – Business Cards</title>
<link href="https://fonts.googleapis.com/css2?family=Montserrat:wght@300;500;600&family=Poppins:wght@400&display=swap" rel="stylesheet">
<style>
  :root {
    --backdrop: #7b7b7b;
    --card-blue: #7babd7;
    --ink-white: #ffffff;
    --art-light: #dedede;
    --art-mid: #c4c4c4;
  }
  * { margin: 0; padding: 0; box-sizing: border-box; }
  html, body {
    width: 1093px;
    height: 1200px;
    overflow: hidden;
    background: var(--backdrop);
  }
  .card {
    position: absolute;
    left: 265px;
    width: 578px;
    height: 356px;
    border-radius: 22px;
    background: var(--card-blue);
    overflow: hidden;
    color: var(--ink-white);
    box-shadow: 3px 4px 0 #111, 5px 8px 14px rgba(0,0,0,0.35);
  }
  .card--front { top: 226px; }
  .card--back  { top: 621px; }

  .figure-art {
    position: absolute;
    bottom: 0;
    border-radius: 14px 14px 0 0;
    background: linear-gradient(180deg, var(--art-light) 0%, var(--art-mid) 100%);
  }
  .card--front .figure-art { left: 330px; width: 178px; top: 10px; }
  .card--back  .figure-art { left: 410px; width: 168px; top: 16px; }

  .brand-name {
    font-family: "Montserrat", sans-serif;
    font-weight: 500;
    line-height: 1;
    letter-spacing: -0.02em;
  }
  .brand-tagline {
    font-family: "Montserrat", sans-serif;
    font-weight: 300;
    line-height: 1;
    letter-spacing: -0.03em;
  }
  .card--front .brand { position: absolute; left: 32px; top: 54px; }
  .card--front .brand-name { font-size: 56px; }
  .card--front .brand-tagline { font-size: 31px; margin-top: 2px; }

  .card--back .brand {
    position: absolute;
    left: 22px;
    top: 180px;
    width: 380px;
    text-align: center;
  }
  .card--back .brand-name { font-size: 72px; }
  .card--back .brand-tagline { font-size: 40px; margin-top: 8px; }

  .person { position: absolute; left: 37px; top: 164px; }
  .person-name {
    font-family: "Montserrat", sans-serif;
    font-weight: 600;
    font-size: 19px;
    letter-spacing: 0;
  }
  .person-role {
    font-family: "Poppins", sans-serif;
    font-size: 17px;
    margin-top: 0;
  }

  .contact-list {
    position: absolute;
    left: 37px;
    top: 244px;
    list-style: none;
    font-family: "Poppins", sans-serif;
    font-size: 17px;
  }
  .contact-item {
    display: flex;
    align-items: center;
    height: 22px;
  }
  .contact-icon {
    width: 15px;
    height: 15px;
    margin-right: 7px;
    flex: none;
  }
</style>
</head>
<body>

  <section class="card card--front">
    <div class="figure-art" role="img" aria-label="Illustration of a human figure seen from behind with the spine highlighted"></div>

    <div class="brand">
      <div class="brand-name">KORVANE</div>
      <div class="brand-tagline">THERAPEUTICS</div>
    </div>

    <div class="person">
      <div class="person-name">DANIEL MERCER</div>
      <div class="person-role">Managing Director</div>
    </div>

    <ul class="contact-list">
      <li class="contact-item">
        <svg class="contact-icon" viewBox="0 0 16 16" aria-hidden="true">
          <path d="M4 1.5l2.2 3-1.4 1.6c.8 1.9 2.3 3.4 4.2 4.2l1.6-1.4 3 2.2-1.3 2.4C7 13.3 2.7 9 2.3 2.8z" fill="#fff"/>
          <path d="M9.5 2.5a4.5 4.5 0 0 1 4 4M9.3 4.8a2.3 2.3 0 0 1 1.9 1.9" stroke="#fff" stroke-width="1.2" fill="none"/>
        </svg>
        044-987 654 321
      </li>
      <li class="contact-item">
        <svg class="contact-icon" viewBox="0 0 16 16" aria-hidden="true">
          <rect x="0.5" y="3" width="15" height="10" fill="#fff"/>
          <path d="M1 3.5l7 5.5 7-5.5M1 12.5l5-4.5M15 12.5l-5-4.5" stroke="var(--card-blue)" stroke-width="1" fill="none"/>
        </svg>
        hello@korvanetherapy.com
      </li>
      <li class="contact-item">
        <svg class="contact-icon" viewBox="0 0 16 16" aria-hidden="true">
          <g stroke="#fff" stroke-width="1.1" fill="none">
            <circle cx="8" cy="8" r="6.8"/>
            <ellipse cx="8" cy="8" rx="3" ry="6.8"/>
            <path d="M1.2 8h13.6M2.3 4.5h11.4M2.3 11.5h11.4"/>
          </g>
        </svg>
        www.korvanetherapy.com
      </li>
    </ul>
  </section>

  <section class="card card--back">
    <div class="figure-art" role="img" aria-label="Illustration of a human figure seen from behind with the spine highlighted"></div>

    <div class="brand">
      <div class="brand-name">KORVANE</div>
      <div class="brand-tagline">THERAPEUTICS</div>
    </div>
  </section>

</body>
</html>
```